Business card needed for the Rydo of Dry Cleaning!

We need a slick business card design for a new company based out of Montreal called Casiers Plimo&Zet inc. (in French) and Plimo&Zet Lockers inc. (in English). We're the Rydo of Laundry. We offer services of dry cleaning, laundry (wash&fold), minor clothing alterations, shoe repair and parcel delivery through 24/7 secured and connected lockers. Ordres are placed through our mobile application. Real time notification are sent to customers when their order is ready for pickup. The lockers will be placed throughout the downtown area, in condo and office towers, where a high density of busy people converge. It is simple, user-friendly, and most importantly convenient. We're the out of the box dry cleaner, literally.

Target Market(s)

1) Professional workers wearing suits daily
2) Campus students living in residences
3) People using laundromats
4) Families with children/yuppies who prefer to use their time doing something else than laundry

Industry/Entity Type

Dry Cleaning

Contact Information for Business Card

Name / Annick-Solène Trudel
Title / CEO & Founder
Company Name / Casiers Plimo&Zet inc. | Plimo&Zet Lockers inc.
Website www.plimozet.ca

Requirements
Must have
• Text Logo: Plimo&Zet - Nettoyeurs 24/7 Cleaners
• Logo on one side and contact info on the other (bilingual)
• Minimalist, pure design
• "We care" for your belongings feeling
• Professional, technological, clean & fresh look
Should not have
• No busy visuals. No rainbow colors.

```html
<!DOCTYPE html>
<html lang="fr">
<head>
<meta charset="utf-8">
<title>Plimo&amp;Zet Lockers inc. – Business Card</title>
<link rel="stylesheet" href="https://fonts.googleapis.com/css2?family=Playfair+Display:wght@400&family=Roboto:wght@300;400&display=swap">
<style>
  :root {
    --stage: #ecedf1;
    --paper: #ffffff;
    --ink: #1d1d1f;
    --brand-blue: #4b5dc6;
    --brand-blue-light: #5a6ed3;
    --on-blue: #ffffff;
  }
  * { margin: 0; padding: 0; box-sizing: border-box; }
  html, body { width: 1200px; height: 892px; overflow: hidden; }
  body {
    background: var(--stage);
    display: flex;
    flex-direction: column;
    align-items: center;
    justify-content: center;
    gap: 38px;
    font-family: "Roboto", Arial, sans-serif;
  }
  .card {
    width: 660px;
    height: 377px;
    background: var(--paper);
    position: relative;
    box-shadow: 0 2px 10px rgba(0,0,0,0.12);
  }
  /* Front: contact side */
  .card-front .company-name {
    position: absolute;
    top: 34px;
    left: 40px;
    font-family: "Playfair Display", Georgia, serif;
    font-weight: 400;
    font-size: 46px;
    letter-spacing: -0.5px;
    color: var(--ink);
    white-space: nowrap;
  }
  .card-front .info-panel {
    position: absolute;
    left: 40px;
    right: 40px;
    top: 128px;
    bottom: 40px;
    background: linear-gradient(160deg, var(--brand-blue-light), var(--brand-blue));
    color: var(--on-blue);
    display: flex;
    align-items: center;
  }
  .person {
    flex: 0 0 296px;
    padding-left: 32px;
    align-self: flex-end;
    padding-bottom: 36px;
  }
  .person-name { font-weight: 300; font-size: 27px; line-height: 1.15; }
  .person-title { font-weight: 300; font-size: 17px; margin-top: 4px; }
  .divider {
    width: 2px;
    height: 82px;
    background: var(--on-blue);
    align-self: flex-start;
    margin-top: 40px;
  }
  .contact-list {
    list-style: none;
    padding-left: 24px;
    align-self: flex-start;
    margin-top: 34px;
    font-size: 17px;
    font-weight: 300;
  }
  .contact-list li { display: flex; align-items: center; gap: 10px; line-height: 30px; white-space: nowrap; }
  .contact-icon { width: 14px; height: 14px; flex: none; }

  /* Back: logo side */
  .card-back { padding: 26px; }
  .card-back .brand-field {
    width: 100%;
    height: 100%;
    background: linear-gradient(160deg, var(--brand-blue-light), var(--brand-blue));
    display: flex;
    align-items: center;
    justify-content: center;
  }
  .brand-name {
    font-family: "Playfair Display", Georgia, serif;
    font-weight: 400;
    font-size: 44px;
    color: var(--on-blue);
    white-space: nowrap;
  }
</style>
</head>
<body>
  <section class="card card-front" aria-label="Card front">
    <h1 class="company-name">Plimo&amp;Zet Lockers inc.</h1>
    <div class="info-panel">
      <div class="person">
        <p class="person-name">Annick-Solène Trudel</p>
        <p class="person-title">CEO &amp; Founder</p>
      </div>
      <div class="divider"></div>
      <ul class="contact-list">
        <li>
          <svg class="contact-icon" viewBox="0 0 14 14" aria-hidden="true">
            <rect width="14" height="14" rx="1.5" fill="#fff"/>
            <path d="M4 3.2l1.6-.4.9 2-1 .8a5.5 5.5 0 0 0 2.9 2.9l.8-1 2 .9-.4 1.6C8 10.3 3.7 6 4 3.2z" fill="#4b5dc6"/>
          </svg>
          514 555-0172
        </li>
        <li>
          <svg class="contact-icon" viewBox="0 0 14 14" aria-hidden="true">
            <rect width="14" height="14" rx="1.5" fill="#fff"/>
            <circle cx="7" cy="7" r="4" fill="none" stroke="#4b5dc6" stroke-width="1.2"/>
            <path d="M3 7h8M7 3c-2 2.5-2 5.5 0 8M7 3c2 2.5 2 5.5 0 8" fill="none" stroke="#4b5dc6" stroke-width="1"/>
          </svg>
          www.plimozet.ca
        </li>
        <li>
          <svg class="contact-icon" viewBox="0 0 14 14" aria-hidden="true">
            <rect width="14" height="14" rx="1.5" fill="#fff"/>
            <rect x="2.5" y="4" width="9" height="6" fill="none" stroke="#4b5dc6" stroke-width="1.1"/>
            <path d="M2.5 4L7 7.5 11.5 4" fill="none" stroke="#4b5dc6" stroke-width="1.1"/>
          </svg>
          casiers@Plimo&amp;Zet inc.
        </li>
      </ul>
    </div>
  </section>

  <section class="card card-back" aria-label="Card back">
    <div class="brand-field">
      <p class="brand-name">Casiers Plimo&amp;Zet inc.</p>
    </div>
  </section>
</body>
</html>
```